Velmarone Website Redesign

We need a redesign of the company website.

We're a company, based in the UK, called Velmarone. We develop software for the Healthcare Industry, used by medical professionals throughout the UK on a daily basis.

We have a suite of tools that form the Velmarone Platform, and all are web-based.

We want to communicate that our software is not only innovative but is the best available, easy to use, and provides exceptional quality and RoI.

Additionally, we want our existing customers to be able to see what else we can offer them.

A site map is attached.
Updates

Hi Everyone,

As we approach the deadline for submissions, we’ve shortlisted threedesigns that we felt were the best of the submissions and have asked thedesigners to make some additional changes and produce some content pages so wecan see what’s beneath the Home page in the rest of the site.

Thank you all for your submissions – there was an awful lot ofdisagreement among everyone here over which designs we thought were best andsome of those that haven’t made it into the final three were very well liked.

Those in the final three have been messaged individually and have theirdesigns as the only non-eliminated ones showing. We would ask at this stagethat anyone not in the final three please do no further work or submitadditional designs as we are approaching the deadline and will not be able toprovide sufficient feedback to allow any changes in a short space of time.

Kind regards,
The Velmarone Team

Target Market(s)

Nurses and medical professionals in western-speaking countries, most notably in the UK.

Predominantly, we expect it will be senior medical staff that will be viewing (and using) our website - some will be existing customers and some will be new or potential customers.

Industry/Entity Type

Medical

Requirements
Must have
• Area to showcase and provide information about products.
• Company information - who we are and why you should choose us.
• News and events - blog, archive newsletters, publications, etc.
• Support section for existing customers - FAQ, Forum, Manuals.
• Contact page.
• We also feel that we'd like to have our telephone number and primary email address visible at all times, with an immediate ability for users to request a demonstration.
Nice to have
• A "My Velmarone" area would be nice at some point, though that's something for further down the line.

```html
<!DOCTYPE html>
<html lang="en">
<head>
<meta charset="utf-8">
<title>Velmarone Health</title>
<link href="https://fonts.googleapis.com/css2?family=Ubuntu:wght@400;500;700&family=Open+Sans:wght@400;600;700&family=Arimo:wght@400&display=swap" rel="stylesheet">
<style>
:root{
  --blue-deep:#0a3aa8;
  --blue-mid:#1a5fd6;
  --blue-light:#3f8ef0;
  --nav-bg:#111;
  --cream:#fdf5e6;
  --heading:#1a5fb4;
  --rule:#5b3fb0;
  --text:#222;
  --footer:#1e2633;
  --footer-bar:#171c26;
  --footer-text:#dfe4ec;
  --btn:#0d4a99;
}
*{box-sizing:border-box;margin:0;padding:0}
html,body{width:842px;height:1200px;overflow:hidden}
body{position:relative;font-family:"Open Sans",sans-serif;color:var(--text);
  background:linear-gradient(100deg,var(--blue-mid) 0%,var(--blue-light) 45%,var(--blue-mid) 100%)}
.abs{position:absolute}
.header{left:0;top:0;width:842px;height:130px;
  background:radial-gradient(ellipse at 75% 70%,#5aa9ff 0%,#1c63e0 35%,#0a37a0 75%,#072a80 100%)}
.brand{left:115px;top:30px;display:flex;align-items:center;gap:9px;font-family:"Ubuntu",sans-serif;font-weight:500;font-size:27px;color:#fff}
.brand-mark{width:14px;height:14px;border-radius:50%;background:#fff}
.tagline{left:138px;top:70px;font-family:"Ubuntu",sans-serif;font-size:12.5px;color:#dce8ff}
.contact{left:520px;top:8px;font-family:"Ubuntu",sans-serif;font-weight:500;font-size:13.5px;color:#fff;line-height:26px}
.nav{left:0;top:130px;width:842px;height:35px;background:linear-gradient(#2a2a2a,var(--nav-bg));display:flex;justify-content:center;align-items:center}
.nav a{font-family:"Arimo",sans-serif;font-size:12.5px;color:#fff;text-decoration:none;padding:0 10px;line-height:28px;border-left:1px solid #555}
.nav a:first-child{border-left:none}
.panel{left:110px;top:166px;width:621px;height:836px;background:#fff}
.welcome{left:111px;top:166px;width:620px;height:305px;background:var(--cream);border-bottom:3px solid #777;
  box-shadow:inset 0 10px 12px -6px #9aa7c4}
.photo{background:linear-gradient(120deg,#f4f4f4,#e2dcd4 60%,#cfc7bd)}
.welcome-photo{left:131px;top:232px;width:312px;height:180px;border:6px solid #e6e6e6;border-radius:4px;box-shadow:0 2px 3px #bbb}
h2{font-family:"Ubuntu",sans-serif;font-weight:400;color:var(--heading);position:absolute}
.rule{position:absolute;height:1.5px;background:var(--rule)}
.copy{font-size:8.2px;line-height:12.4px;letter-spacing:.2px;position:absolute}
.copy p+p{margin-top:12.4px}
.demo-btn{left:133px;top:525px;width:160px;height:39px;background:linear-gradient(#1b6fe0,#0c4fb8);border:2px solid #4b93f0;
  font-family:"Ubuntu",sans-serif;font-weight:700;font-size:15.5px;color:#fff;display:flex;align-items:center;justify-content:center}
.login{left:133px;top:573px;width:160px;height:139px;background:#f0f0f0;border-radius:5px}
.login label{position:absolute;left:15px;font-weight:700;font-size:7.5px}
.login .field{position:absolute;left:12px;width:131px;height:20px;border:1px solid #777;background:#fafafa}
.signin{position:absolute;left:45px;top:108px;width:54px;height:19px;background:var(--btn);border-radius:3px;color:#fff;font-size:8px;font-weight:700;display:flex;align-items:center;justify-content:center}
.more{position:absolute;font-size:7.3px;font-weight:700}
.divider{left:320px;top:523px;height:442px;border-left:1px dotted #999}
.thumb{position:absolute;left:350px;width:80px;height:53px;border:1px solid #555;border-radius:4px}
.platform-photo{left:349px;top:575px;width:153px;height:101px;border:3px solid #1a5fc8;border-radius:5px;background:linear-gradient(120deg,#eef2f4,#d9dcd2 50%,#b9c3c9)}
.item-title{font-weight:700;letter-spacing:.5px}
.footer{left:0;top:1002px;width:842px;height:171px;background:var(--footer)}
.footer-col{position:absolute;top:1019px}
.footer-col h3{font-family:"Ubuntu",sans-serif;font-weight:400;font-size:13.5px;color:#fff;margin-bottom:6px}
.footer-col li{list-style:none;font-size:7.5px;letter-spacing:.5px;color:var(--footer-text);line-height:14px}
.footer-col li::before{content:"\203A\203A";font-weight:700;margin-right:3px}
.footer-bar{left:0;top:1173px;width:842px;height:27px;background:var(--footer-bar);color:var(--footer-text);font-size:8px;letter-spacing:.3px;display:flex;align-items:center;justify-content:center;white-space:pre}
</style>
</head>
<body>
<header class="abs header"></header>
<div class="abs brand"><span class="brand-mark"></span>Velmarone Health</div>
<div class="abs tagline">Software for modern clinical care</div>
<div class="abs contact">Call : +44 (0) 208 555 0142<br>Email: support@velmarone.com</div>

<nav class="abs nav">
  <a>Home</a><a>Products &amp; Services</a><a>About Velmarone</a><a>News &amp; Events</a><a>Support</a><a>Contact Velmarone</a><a>My Velmarone</a>
</nav>

<div class="abs panel"></div>
<section class="abs welcome"></section>
<div class="abs welcome-photo photo" role="img" aria-label="Clinician in a white coat beside a laboratory microscope"></div>
<h2 style="left:472px;top:206px;font-size:19px">Welcome To Velmarone</h2>
<div class="rule" style="left:461px;top:234px;width:247px"></div>
<div class="copy" style="left:460px;top:246px;width:245px">
  <p>In today’s changing environment, healthcare organisa-tions globally are faced with conflicting challenges; to reduce costs while offering improved healthcare ser-vices to patients.</p>
  <p>VELMARONE solutions exploit opportunities offered by the latest technological advances. Our goal is to help:<br>Reduce clinical errors<br>Improve patient care<br>Improve efficiency</p>
  <p>With our integrated solutions, robust and secure infra-structure and by leveraging our experience, skills and partnerships, Velmarone aims to become one of the leading international service and solution providers to the healthcare industry.</p>
</div>

<div class="abs demo-btn">REQUEST A DEMO</div>
<div class="abs login">
  <label style="top:17px">USER ID</label>
  <div class="field" style="top:29px"></div>
  <label style="top:56px">PASSWORD</label>
  <div class="field" style="top:68px"></div>
  <div class="signin">Sign in</div>
</div>

<h2 style="left:169px;top:756px;font-size:15px">Latest News</h2>
<div class="rule" style="left:131px;top:781px;width:160px"></div>
<div class="copy" style="left:130px;top:787px;width:175px">Lorem Ipsum is simply dummy text of the printing and typesetting industry.</div>
<div class="more" style="left:261px;top:826px">More ››</div>
<h2 style="left:176px;top:849px;font-size:16px">Our Blog</h2>
<div class="rule" style="left:131px;top:875px;width:160px"></div>
<div class="copy" style="left:131px;top:883px;width:175px">Lorem Ipsum is simply dummy text of the printing and typesetting industry. Lorem Ipsum has been the industry's standard dummy text ever since the 1500s unchanged</div>
<div class="more" style="left:265px;top:947px">More ››</div>

<div class="abs divider"></div>

<h2 style="left:350px;top:497px;font-size:19px">Velmarone Solutions</h2>
<div class="rule" style="left:341px;top:522px;width:368px"></div>
<div class="copy" style="left:350px;top:529px;width:360px">Velmarone works in partnership with hospitals and healthcare professionals. Our unique approach, our partnerships with clinical specialists and our technology platform enables us to deliver highly robust and fit-for-purpose solutions.</div>
<div class="abs platform-photo" role="img" aria-label="Doctor with stethoscope standing in a clinic office"></div>
<div class="copy" style="left:513px;top:574px;width:198px"><span class="item-title">Our Platform</span><br>Our technology platform, the Care Workflow Hub, is a robust service based framework that supports our acceler-ated application development approach. It enables interoperability and integration between Velmarone software modules and other hospital/healthcare systems.</div>

<div class="copy item-title" style="left:454px;top:725px">Our Products and Services Include</div>

<div class="thumb photo" style="top:730px" role="img" aria-label="Clinicians reviewing data on a screen"></div>
<div class="copy" style="left:454px;top:750px;width:250px"><span class="item-title">Clinical Systems</span><br>Lorem Ipsum is simply dummy text of the printing and typesetting industry.</div>
<div class="more" style="left:663px;top:790px">More ››</div>

<div class="thumb photo" style="top:801px;background:linear-gradient(120deg,#fff,#f0d9c6 50%,#c9ccd2)" role="img" aria-label="Hands typing on a laptop keyboard"></div>
<div class="copy" style="left:454px;top:812px;width:250px"><span class="item-title">Clinical Audit Tools</span><br>Lorem Ipsum is simply dummy text of the printing and typesetting industry.</div>
<div class="more" style="left:659px;top:852px">More ››</div>

<div class="thumb photo" style="top:871px;background:linear-gradient(90deg,#b9b7c6 55%,#cfdcef 56%,#e6d2c4)" role="img" aria-label="Finger touching a screen"></div>
<div class="copy" style="left:454px;top:887px;width:250px"><span class="item-title">Technology Services</span><br>Lorem Ipsum is simply dummy text of the printing and typesetting industry.</div>
<div class="more" style="left:657px;top:927px">More ››</div>

<footer class="abs footer"></footer>
<div class="footer-col" style="left:135px"><h3>Product &amp; Services</h3><ul><li>Clinical Audit</li><li>Clinical Systems</li><li>Software Development</li><li>Clinical Consultancy</li><li>Case Studies</li><li>Demos</li></ul></div>
<div class="footer-col" style="left:303px"><h3>About Velmarone</h3><ul><li>Leadership Team</li><li>Advisory Board</li><li>Partnerships</li><li>Experienced Clinical Staff</li><li>Medical Solutions Architects</li><li>Client List</li></ul></div>
<div class="footer-col" style="left:467px"><h3>News &amp; Events</h3><ul><li>Monthly News Letters</li><li>Publications</li><li>Events</li><li>Velmarone News Blog</li></ul></div>
<div class="footer-col" style="left:627px"><h3>Support</h3><ul><li>FAQ</li><li>Manuals</li><li>Publications</li><li>User Forums</li></ul></div>
<div class="abs footer-bar">Home | Products &amp; Services | About Velmarone | News &amp; Events  | Support | Contact Velmarone | My Velmarone</div>
</body>
</html>
```